Web Design Project

blaze guard safety & solutions needs a new web design to go with its new logo design

we provide services such as instillation of fire sprinklers, fire hydrants , fire hose reels as well as fire extinguishers and fire blankets.

we can service these as well and also do the preventitave maintaince of these too.

we can do flow testing of sprinklers,hydrants & hosereels and test back flow prevention devices as well

old page is bgss-example.com.au

Industry/Entity Type

Defence

```html
<!DOCTYPE html>
<html lang="en">
<head>
<meta charset="utf-8">
<title>Blaze Guard Safety & Solutions</title>
<link href="https://fonts.googleapis.com/css2?family=PT+Sans:wght@400;700&family=Arimo:wght@400;700&display=swap" rel="stylesheet">
<style>
:root{
  --red:#c8111a;
  --red-dark:#9e0c12;
  --blue:#1ba3d8;
  --ink:#3a3a3a;
  --muted:#555;
  --line:#d8d8d8;
  --footer:#e3e3e3;
  --white:#fff;
}
*{box-sizing:border-box;margin:0;padding:0}
html,body{width:1183px;height:1200px;overflow:hidden}
body{
  position:relative;
  font-family:"Arimo",Arial,sans-serif;color:var(--ink);
  background:linear-gradient(#2f2f2f 0,#6a6a6a 160px,#d9d9d9 420px,#fff 560px,#fff 720px,#e4e4e4 722px,#f2f2f2 900px,#fff 1110px);
}
.abs{position:absolute}
.brand{left:126px;top:22px;width:240px;color:var(--white);font-family:"PT Sans",sans-serif}
.brand-name{display:flex;align-items:center;gap:10px;font-size:19px;font-weight:700;line-height:1.1}
.brand-mark{width:32px;height:32px;border-radius:50%;background:var(--red);flex:none}
.contact-link{right:104px;top:12px;color:var(--white);font:700 13px "PT Sans",sans-serif;display:flex;align-items:center;gap:7px}
.search{right:104px;top:50px;width:230px;height:27px;display:flex;border-radius:4px;overflow:hidden;background:var(--white);border:1px solid #999}
.search-field{flex:1;display:flex;align-items:center;gap:6px;padding-left:6px;color:#999;font-size:11px}
.search-btn{width:62px;background:linear-gradient(#e0232b,var(--red-dark));color:var(--white);font:700 13px "PT Sans",sans-serif;display:flex;align-items:center;justify-content:center}
.nav{left:106px;top:106px;width:970px;height:50px;border-radius:6px 6px 0 0;background:linear-gradient(#4a4a4a,#2c2c2c);display:flex;align-items:flex-end;padding-left:17px;font:400 16px "PT Sans",sans-serif;color:#eee}
.nav-item{height:42px;display:flex;align-items:center;padding:0 22px}
.nav-item.active{background:var(--white);color:#222;font-weight:700;border-radius:4px 4px 0 0;padding:0 14px}
.caret{display:inline-block;border:4px solid transparent;border-top-color:#eee;margin:5px 0 0 5px}
.nav-phone{margin-left:auto;padding-right:16px;height:42px;display:flex;align-items:center;gap:8px;font-weight:700}
.hero-frame{left:106px;top:156px;width:970px;height:396px;background:var(--white);border-radius:0 0 6px 6px;box-shadow:0 12px 14px -8px rgba(0,0,0,.45)}
.hero-photo{position:absolute;left:10px;top:10px;width:950px;height:377px;border-radius:6px;
  background:radial-gradient(ellipse at 62% 50%,#e8a52a 0,#c9661a 25%,#6e3a1c 55%,#2a2220 85%)}
.hero-title{position:absolute;left:26px;top:30px;color:var(--white);font-family:"PT Sans",sans-serif;line-height:1}
.hero-title .big{font-size:72px;letter-spacing:-2px}
.hero-title .sub{font-size:40px;margin:4px 0 0 4px;letter-spacing:-1px}
.hero-lead{position:absolute;left:26px;top:155px;width:345px;font:400 18px/23px "PT Sans",sans-serif;color:var(--white)}
.hero-lead span{background:var(--red);padding:0 5px;box-decoration-break:clone;-webkit-box-decoration-break:clone}
.btn-browse{position:absolute;left:28px;top:298px;width:228px;height:55px;border-radius:6px;background:linear-gradient(#e42a30,var(--red-dark));color:var(--white);font:700 23px "PT Sans",sans-serif;display:flex;align-items:center;padding-left:15px;gap:26px;box-shadow:0 3px 6px rgba(0,0,0,.5)}
.thumbs{position:absolute;right:18px;bottom:12px;display:flex;gap:6px}
.thumb{width:53px;height:48px;border:2px solid var(--white);border-radius:6px}
.stats{left:106px;top:572px;width:970px;height:169px;border-radius:6px;background:linear-gradient(#ededed,#fafafa 60%,#fff);box-shadow:0 2px 4px rgba(0,0,0,.15);display:flex}
.stat{flex:1;display:flex;flex-direction:column;align-items:center;text-align:center;border-right:1px solid var(--line);padding-top:22px}
.stat:last-child{border-right:0}
.stat-visual{height:92px;display:flex;align-items:center;justify-content:center}
.stat h3{font:700 13px "PT Sans",sans-serif;color:#333}
.stat p{font-size:11px;color:var(--muted);line-height:13px;margin-top:3px;max-width:210px}
.num48{font:700 82px "PT Sans",sans-serif;color:#cfcfcf;text-shadow:1px 1px 0 #999,3px 3px 4px rgba(0,0,0,.2);letter-spacing:-3px}
.million{font-family:"PT Sans",sans-serif;line-height:1}
.million b{display:block;font-size:34px;color:var(--blue);letter-spacing:-1px}
.million span{font-size:15px;font-weight:700;color:#222}
.exit{width:128px;height:62px;background:linear-gradient(#3cb449,#137a24);border-radius:3px;display:flex;align-items:center;justify-content:center}
.trolley{width:70px;height:88px;background:linear-gradient(#c9a47a,#8a7d70);border-radius:4px}
.welcome{left:108px;top:762px;width:650px}
.welcome h1{font:700 31px "PT Sans",sans-serif;color:var(--red);letter-spacing:-.3px}
.welcome h2{font:700 15px/19px "PT Sans",sans-serif;color:var(--blue);margin-top:10px}
.welcome p{font-size:12px;line-height:19px;color:var(--muted);margin-top:18px}
.aside-line{left:770px;top:760px;width:1px;height:360px;background:linear-gradient(#ddd,transparent)}
.quote{left:783px;top:757px;width:293px;height:160px;border-radius:6px;background:linear-gradient(135deg,#d51c24,var(--red-dark));color:var(--white);padding:13px 13px;font-family:"PT Sans",sans-serif;overflow:hidden}
.quote .pre{font-size:20px}
.quote .big{font-size:40px;font-weight:700;line-height:.95}
.quote p{font-size:12px;font-weight:700;line-height:14px;margin-top:17px;width:210px}
.quote-bubble{position:absolute;right:6px;top:-2px;width:110px;height:95px;border-radius:18px;background:linear-gradient(#31c4ec,#0e7fb0);opacity:.9}
.promo{left:783px;top:926px;width:293px;height:157px;border-radius:6px;background:linear-gradient(#fff,#e6e6e6);box-shadow:0 2px 5px rgba(0,0,0,.25)}
.promo-photo{position:absolute;left:14px;top:22px;width:95px;height:112px;background:linear-gradient(135deg,#2a4ea0,#f0d230);border-radius:4px}
.promo-body{position:absolute;left:122px;top:14px;width:160px}
.promo h3{font:700 19px/19px "PT Sans",sans-serif;color:var(--red);width:150px}
.promo p{font-size:12px;line-height:16px;color:var(--muted);margin-top:9px}
.btn-quote{margin-top:10px;width:124px;height:30px;border-radius:4px;background:linear-gradient(#e42a30,var(--red-dark));color:var(--white);font-size:11px;font-weight:700;display:flex;align-items:center;justify-content:space-between;padding:0 8px}
.btn-quote i{width:13px;height:13px;border-radius:50%;background:#6e0a0e;display:flex;align-items:center;justify-content:center}
.footer{left:0;top:1110px;width:1183px;height:90px;background:var(--footer);font-size:12px}
.footer .copy{position:absolute;left:112px;top:18px;color:var(--blue)}
.footer .links{position:absolute;left:112px;top:38px;color:#444}
.footer .addr{position:absolute;right:106px;top:18px;color:var(--blue)}
.footer .mail{position:absolute;right:106px;top:38px;color:#444}
</style>
</head>
<body>
<header>
  <div class="abs brand">
    <div class="brand-name"><span class="brand-mark"></span>Blaze Guard Safety &amp; Solutions</div>
  </div>
  <div class="abs contact-link">
    <svg width="16" height="11" viewBox="0 0 16 11"><rect x="0.5" y="0.5" width="15" height="10" fill="#ddd" stroke="#999"/><path d="M1 1l7 5 7-5" fill="none" stroke="#888"/></svg>
    Contact Us
  </div>
  <div class="abs search">
    <div class="search-field">
      <svg width="13" height="13" viewBox="0 0 13 13"><circle cx="5" cy="5" r="4" fill="none" stroke="#999" stroke-width="1.5"/><path d="M8 8l4 4" stroke="#999" stroke-width="2"/></svg>
      enter keyword
    </div>
    <div class="search-btn">Search</div>
  </div>
  <nav class="abs nav">
    <span class="nav-item active">Home</span>
    <span class="nav-item">Products</span>
    <span class="nav-item">Services</span>
    <span class="nav-item">Technical Information<i class="caret"></i></span>
    <span class="nav-item">Company Information<i class="caret"></i></span>
    <span class="nav-phone">
      <svg width="16" height="18" viewBox="0 0 16 18"><path d="M3 1l3 4-2 2c1 3 3 5 6 6l2-2 4 3-2 3C7 17 0 10 1 3z" fill="#ccc"/></svg>
      (121) 555-0142
    </span>
  </nav>
</header>

<section class="abs hero-frame">
  <div class="hero-photo" role="img" aria-label="Firefighters in yellow gear tackling a large blaze">
    <div class="hero-title"><div class="big">Fire, Safety</div><div class="sub">&amp; First aid equipment</div></div>
    <p class="hero-lead"><span>Blaze Guard is an owner operated business so our reputation is our guarantee to do the best job we possibly can.</span></p>
    <div class="btn-browse">Browse products
      <svg width="9" height="10" viewBox="0 0 9 10"><path d="M0 0l9 5-9 5z" fill="#fff"/></svg>
    </div>
    <div class="thumbs">
      <div class="thumb" role="img" aria-label="Fire extinguisher" style="background:linear-gradient(#eee,#c33)"></div>
      <div class="thumb" role="img" aria-label="Fire hose reel" style="background:linear-gradient(#f44,#a00)"></div>
      <div class="thumb" role="img" aria-label="Fire blanket" style="background:linear-gradient(#e22,#b00)"></div>
      <div class="thumb" role="img" aria-label="Hard hat" style="background:linear-gradient(#e6c12a,#556)"></div>
    </div>
  </div>
</section>

<section class="abs stats">
  <div class="stat">
    <div class="stat-visual"><span class="num48">48</span></div>
    <h3>Blaze Guard Safety &amp; Solutions</h3>
    <p>Best Products</p>
  </div>
  <div class="stat">
    <div class="stat-visual"><div class="million"><b>3 MILLION</b><span>FIRE EXTINGUISHERS SOLD</span></div></div>
    <h3>Thousands of satisfied customers</h3>
    <p>100% Alberta Owned and Operated</p>
  </div>
  <div class="stat">
    <div class="stat-visual" style="height:90px">
      <div class="exit"><svg width="40" height="30" viewBox="0 0 40 30"><path d="M4 15h22M18 5l12 10-12 10" fill="none" stroke="#fff" stroke-width="6"/></svg></div>
    </div>
    <h3>Emergency Services</h3>
    <p>24 hours a day, 7 days a week, nights and holidays included.</p>
  </div>
  <div class="stat">
    <div class="stat-visual"><div class="trolley" role="img" aria-label="Hand truck carrying a cardboard box"></div></div>
    <h3>Ordering Made Easy</h3>
    <p>Order by phone, fax or mail. Our sales staff will be happy to assist you</p>
  </div>
</section>

<main class="abs welcome">
  <h1>Welcome to Blaze Guard Safety &amp; Solutions</h1>
  <h2>your source for not only quality fire extinguishers, but fire alarms, emergency &amp; exit lighting, respirators, hard hats, safety glasses, first aid products, eyewash stations&nbsp; and much, much more.</h2>
  <p>Blaze Guard is a fire protection company situated on the Central Coast of NSW and is currently servicing the Sydney, Central Coast and Hunter areas, We are always looking for new clients who are not happy with there current service providers and are looking for a Competitive priced alternative. Blaze Guard will come to your site and assess your fire service assets and provide a full quotation on a 12 month service contract.</p>
  <p>Blaze Guard can also supply quotations for any alterations to your Sprinklers,Hydrants &amp; Hose reel systems along with your fire detection and emergency lighting.</p>
  <p>Blaze Guard is an owner operated business, so our reputation is our guarantee to do the best job we possibly can.<br>We use only manufacturer recommended parts and U.L.C. listed chemicals for recharging your fire equipment.</p>
</main>

<div class="abs aside-line"></div>

<aside class="abs quote">
  <div class="quote-bubble" role="img" aria-label="Blue speech bubble with quotation marks"></div>
  <div class="pre">Get a Product</div>
  <div class="big">QUOTE</div>
  <p>Our Quotation Generator will allow you to add items to your cart and submit a NO OBLIGATION request for quotation!</p>
</aside>

<aside class="abs promo">
  <div class="promo-photo" role="img" aria-label="Box of foam ear plugs"></div>
  <div class="promo-body">
    <h3>Fire Hose Reels and Hydrants</h3>
    <p>Lorem ipsum dolor sit amet, cons adipiscing elit.</p>
    <div class="btn-quote">Request a quote <i><svg width="6" height="5" viewBox="0 0 6 5"><path d="M0 0h6L3 5z" fill="#fff"/></svg></i></div>
  </div>
</aside>

<footer class="abs footer">
  <div class="copy">Copyright 2011, blazeguardsafety-example.com. All rights reserved.</div>
  <div class="links">sitemap &nbsp;|&nbsp; contact &nbsp;|&nbsp; privacy policy</div>
  <div class="addr">88 Harbour Road, Gosford, NSW 2250</div>
  <div class="mail">info@bgss-example.com.au</div>
</footer>
</body>
</html>
```